Dog Shampoo producer needs a bottle Sticker design

We need a Sticker design for our new Dog Shampoo product. The brand is "Velmo". This is for one of our product for smaller dogs with emphasis on no-tear and paraben-free formula. Photos of the bottle design are attached. Dimensions on the bottle drawings are in milimeters. Sticker shape and sizes should follow the shape and size of bottle. Bottle volume is 500ml.

The back sticker contains a space for barcode, ingredients (please put 7 to 8 ingredient list common for shampoo, we can update later), have this idea for benefit: formulated by people who care: paraben-free and no-tear formula for healthier and happier dogs, distributed by: PT. Velmo Indonesia

Target Market(s)

Young, sociable, and connected dog owners who often post photos of their activities with their dogs on social media.

Industry/Entity Type

Product

Font styles to use
Decorative

Colors

Designer to choose colors to be used in the design.

Requirements
Must have
• "no-tear" and "paraben-free" texts written on the label to show the product's unique selling point
Nice to have
• picture or drawing of a dog.

```html
<!DOCTYPE html>
<html lang="en">
<head>
<meta charset="utf-8">
<title>Velmo Puppy Shampoo – Label Options</title>
<link rel="stylesheet" href="https://fonts.googleapis.com/css2?family=Rozha+One&family=Oswald:wght@400;500;600&family=Saira+Condensed:wght@700&family=Kaushan+Script&family=Playfair+Display:ital,wght@1,700&family=Courgette&family=Open+Sans:wght@300;400&display=swap">
<style>
  :root {
    --magenta: #c92a8a;
    --magenta-deep: #a5206f;
    --leaf-green: #8dc33e;
    --tan: #d2a686;
    --tan-badge: #cfa485;
    --brown: #8b4a33;
    --grey-text: #8f8f8f;
    --ink: #2b2b2b;
    --bone: #3b4049;
    --number-grey: #c2c2c2;
    --cream: #f3e3c8;
    --paper: #ffffff;
    --frame: #9a9a9a;
  }
  html, body { margin: 0; padding: 0; overflow: hidden; background: var(--paper); }
  .sheet { display: block; width: 1200px; height: 846px; }
  .sheet-frame { fill: none; stroke: var(--frame); stroke-width: 1; }
  .label-outline { stroke: #6b6b6b; stroke-width: 1; }
  .brand-serif { font-family: "Rozha One", serif; }
  .tagline-condensed { font-family: "Oswald", sans-serif; font-weight: 500; }
  .claim { font-family: "Saira Condensed", sans-serif; font-weight: 700; fill: var(--ink); }
  .badge-text { font-family: "Kaushan Script", cursive; fill: #fff; }
  .volume { font-family: "Open Sans", sans-serif; }
  .option-number { font-family: "Open Sans", sans-serif; font-weight: 300; font-size: 44px; fill: var(--number-grey); text-anchor: middle; }
  .brand-italic { font-family: "Playfair Display", serif; font-style: italic; font-weight: 700; }
  .benefit { font-family: "Courgette", cursive; font-size: 21px; fill: var(--ink); text-anchor: middle; }
  .pill-text { font-family: "Courgette", cursive; font-size: 22px; }
</style>
</head>
<body>
<svg class="sheet" viewBox="0 0 1200 846" xmlns="http://www.w3.org/2000/svg">
  <defs>
    <clipPath id="label-five-shape">
      <path d="M82,110 Q237,40 392,110 L392,710 Q237,780 82,710 Z"/>
    </clipPath>
    <linearGradient id="tan-fade" x1="0" y1="0" x2="0.55" y2="0.75">
      <stop offset="0" stop-color="#d0a282"/>
      <stop offset="0.35" stop-color="#e6c7ae"/>
      <stop offset="0.6" stop-color="#fbf4ee"/>
      <stop offset="1" stop-color="#ffffff"/>
    </linearGradient>
    <radialGradient id="tan-corner" cx="0" cy="1" r="0.55">
      <stop offset="0" stop-color="#d6ab8b" stop-opacity="0.9"/>
      <stop offset="1" stop-color="#d6ab8b" stop-opacity="0"/>
    </radialGradient>
    <linearGradient id="gold-sheen" x1="0" y1="0" x2="1" y2="0">
      <stop offset="0" stop-color="#d7a543"/>
      <stop offset="0.3" stop-color="#f0d47a"/>
      <stop offset="0.55" stop-color="#f8eb9c"/>
      <stop offset="0.8" stop-color="#e6c263"/>
      <stop offset="1" stop-color="#b08337"/>
    </linearGradient>
    <linearGradient id="gold-ring" x1="0" y1="0" x2="1" y2="1">
      <stop offset="0" stop-color="#c8933a"/>
      <stop offset="0.5" stop-color="#f3db86"/>
      <stop offset="1" stop-color="#b7862f"/>
    </linearGradient>
    <linearGradient id="puppy-tones" x1="0" y1="0" x2="0" y2="1">
      <stop offset="0" stop-color="#f1dfc6"/>
      <stop offset="1" stop-color="#e2c3a0"/>
    </linearGradient>
  </defs>

  <rect class="sheet-frame" x="0.5" y="0.5" width="1199" height="845"/>

  <!-- Option 5 -->
  <g class="label label-five">
    <path class="label-outline" d="M82,110 Q237,40 392,110 L392,710 Q237,780 82,710 Z" fill="#fff"/>
    <g clip-path="url(#label-five-shape)">
      <rect class="brand-band" x="108" y="0" width="114" height="500" fill="var(--magenta)"/>
    </g>
    <text class="brand-serif" transform="translate(208,298) rotate(-90)" text-anchor="middle" font-size="128" fill="#fff" textLength="350" lengthAdjust="spacingAndGlyphs">Velmo</text>
    <text class="tagline-condensed" transform="translate(266,305) rotate(-90)" text-anchor="middle" font-size="40" fill="var(--grey-text)" textLength="350" lengthAdjust="spacingAndGlyphs">SOFT &amp; FLUFFY SHAMPOO</text>
    <rect class="puppy-photo" role="img" aria-label="Photo of a small puppy in a red scarf and hat" x="106" y="495" width="124" height="195" rx="40" fill="url(#puppy-tones)"/>
    <path class="no-tear-badge" d="M234,578 Q300,546 374,558 Q370,600 302,606 Q252,612 234,598 Z" fill="var(--leaf-green)"/>
    <text class="badge-text" transform="translate(302,592) rotate(-8)" text-anchor="middle" font-size="28">no-tear</text>
    <text class="claim" x="302" y="678" text-anchor="middle" font-size="28">PARABEN-FREE</text>
    <text class="volume" x="246" y="731" text-anchor="middle" font-size="26" fill="#444">500ml</text>
  </g>

  <!-- Option 6 -->
  <g class="label label-six">
    <path class="label-outline" d="M440,90 C500,80 545,122 600,112 C660,100 705,86 758,100 L758,690 C720,682 690,745 620,740 C560,735 500,690 440,702 Z" fill="url(#tan-fade)"/>
    <path d="M440,90 C500,80 545,122 600,112 C660,100 705,86 758,100 L758,690 C720,682 690,745 620,740 C560,735 500,690 440,702 Z" fill="url(#tan-corner)"/>
    <text class="volume" x="696" y="134" text-anchor="middle" font-size="21" font-weight="400" fill="#fff">500ml</text>
    <g class="measure-lines" fill="#fff">
      <rect x="636" y="144" width="112" height="5"/>
      <rect x="636" y="163" width="112" height="5" opacity="0.95"/>
      <rect x="636" y="182" width="112" height="5" opacity="0.9"/>
      <rect x="636" y="201" width="112" height="5" opacity="0.85"/>
      <rect x="636" y="220" width="112" height="5" opacity="0.8"/>
      <rect x="636" y="239" width="112" height="5" opacity="0.75"/>
      <rect x="636" y="258" width="112" height="5" opacity="0.7"/>
      <rect x="636" y="277" width="112" height="5" opacity="0.6"/>
      <rect x="636" y="296" width="112" height="5" opacity="0.5"/>
      <rect x="636" y="315" width="112" height="5" opacity="0.4"/>
      <rect x="636" y="334" width="112" height="5" opacity="0.3"/>
      <rect x="636" y="353" width="112" height="5" opacity="0.22"/>
      <rect x="636" y="372" width="112" height="5" opacity="0.15"/>
      <rect x="636" y="391" width="112" height="5" opacity="0.1"/>
      <rect x="636" y="410" width="112" height="5" opacity="0.06"/>
    </g>
    <text class="brand-serif" transform="translate(560,348) rotate(-90)" text-anchor="middle" font-size="100" fill="var(--brown)" textLength="395" lengthAdjust="spacingAndGlyphs">VELMO</text>
    <text class="tagline-condensed" transform="translate(611,345) rotate(-90)" text-anchor="middle" font-size="37" fill="var(--brown)" textLength="360" lengthAdjust="spacingAndGlyphs">SOFT &amp; FLUFFY SHAMPOO</text>
    <path class="no-tear-badge" d="M478,584 Q520,560 562,568 Q560,600 522,604 Q492,608 478,598 Z" fill="var(--tan-badge)"/>
    <text class="badge-text" transform="translate(520,592) rotate(-8)" text-anchor="middle" font-size="20">no-tear</text>
    <text class="claim" x="524" y="640" text-anchor="middle" font-size="20">PARABEN-FREE</text>
    <rect class="puppy-photo" role="img" aria-label="Photo of a lying puppy" x="588" y="535" width="147" height="165" rx="40" fill="url(#puppy-tones)"/>
  </g>

  <!-- Option 7 -->
  <g class="label label-seven">
    <path class="label-outline" d="M808,120 Q970,50 1132,120 L1132,750 Q970,820 808,750 Z" fill="url(#gold-sheen)"/>
    <ellipse class="brand-oval-ring" cx="963" cy="240" rx="200" ry="97" transform="rotate(-6 963 240)" fill="url(#gold-ring)"/>
    <ellipse class="brand-oval" cx="963" cy="240" rx="186" ry="86" transform="rotate(-6 963 240)" fill="var(--magenta)"/>
    <text class="brand-italic" x="963" y="275" text-anchor="middle" font-size="92" fill="#fff">Velmo</text>
    <rect class="pill-puppy" x="848" y="320" width="120" height="44" rx="22" fill="var(--magenta-deep)"/>
    <rect class="pill-shampoo" x="948" y="320" width="128" height="44" rx="22" fill="#f8f0a2"/>
    <text class="pill-text" x="898" y="350" text-anchor="middle" fill="#fff">Puppy</text>
    <text class="pill-text" x="1012" y="350" text-anchor="middle" fill="var(--magenta)">Shampoo</text>
    <text class="benefit" x="965" y="420">Gently cleans</text>
    <text class="benefit" x="965" y="454">while soothing dry,</text>
    <text class="benefit" x="965" y="488">itchy or sensitive skin</text>
    <rect class="dog-line-art" role="img" aria-label="Gold line drawing of a sitting bulldog" x="945" y="510" width="135" height="130" rx="30" fill="#e9cb78" opacity="0.7"/>
    <path class="no-tear-badge" d="M838,596 Q888,572 940,582 Q938,618 888,622 Q852,626 838,614 Z" fill="var(--magenta-deep)"/>
    <text class="badge-text" transform="translate(888,606) rotate(-8)" text-anchor="middle" font-size="22">no-tear</text>
    <text class="claim" x="965" y="681" text-anchor="middle" font-size="31">PARABEN-FREE</text>
    <g class="bone-icon" fill="var(--bone)">
      <rect x="944" y="698" width="42" height="12" rx="4"/>
      <circle cx="942" cy="697" r="8"/>
      <circle cx="942" cy="711" r="8"/>
      <circle cx="988" cy="697" r="8"/>
      <circle cx="988" cy="711" r="8"/>
    </g>
  </g>

  <text class="option-number" x="228" y="814">5</text>
  <text class="option-number" x="600" y="814">6</text>
  <text class="option-number" x="973" y="814">7</text>
</svg>
</body>
</html>
```